Long Established Local Fencing (not swords) Business needs fresh Business Cards

We need fresh double sided business cards for our Fencing Construction business, we are looking for something with our new logo design added, and maybe a photo background ?
We recently had cards made from Cardlyne and we were horrified with what we got back, the quality was terrible, so am looking for high quality format for good printing company to make.
We install Steelmora, Timber paling, Aluminium Slat Screening, Picket (timber and aluminium) and most other fencing installations.
Our website is brankelrails.com.au should you like to learn a bit more.
We do have logo in other formats if required.
We have been in business for over 35 years and we have used this as a "motto" it is on our signage

Industry/Entity Type

Construction

Contact Information for Business Card

Open to ideas, we need 3 x different cards, one generic with no name and 2 x others each with 1 of our bosses name on each, I will put into upload files.

Colors
ec1f27
000000
606060
f5f5f5

Requirements
Must have
• Company Name and Logo
• Address
• Contact details, phone, website, email etc
• Small space to write notes when leaving card at residence
Nice to have
• Our motto "Servicing the Peninsula for over 35 years"

```html
<!DOCTYPE html>
<html lang="en">
<head>
<meta charset="utf-8">
<title>Brankel Rails – Business Cards</title>
<link href="https://fonts.googleapis.com/css2?family=Archivo+Black&family=Exo+2:wght@300;400&display=swap" rel="stylesheet">
<style>
  :root {
    --red: #ec1f27;
    --black: #000000;
    --grey: #606060;
    --paper: #ffffff;
    --backdrop: #f5f5f5;
    --photo-a: linear-gradient(160deg, #8fa57a 0%, #4f6a3c 55%, #6d6a5e 100%);
    --photo-b: linear-gradient(170deg, #9fc2e4 0%, #2f3b5c 45%, #3d4a32 100%);
    --photo-c: linear-gradient(165deg, #c9d7e2 0%, #5d7a46 50%, #6b6f74 100%);
  }
  * { box-sizing: border-box; margin: 0; padding: 0; }
  html, body { width: 1200px; height: 960px; overflow: hidden; background: var(--backdrop); }
  .canvas { position: relative; width: 1200px; height: 960px; }
  .card {
    position: absolute; left: 250px; width: 700px; height: 428px;
    background: var(--paper); overflow: hidden;
    box-shadow: 0 6px 18px rgba(0,0,0,.12);
    font-family: "Exo 2", sans-serif; color: var(--black);
  }
  .card--front { top: 34px; }
  .card--back { top: 498px; }
  .card__shapes { position: absolute; inset: 0; }

  .brand { position: absolute; display: flex; align-items: center; gap: 10px; }
  .brand__dot { width: 22px; height: 22px; border-radius: 50%; background: var(--red); flex: none; }
  .brand__name {
    font-family: "Archivo Black", sans-serif; font-size: 30px; line-height: 1;
    color: var(--black); letter-spacing: .5px;
  }
  .card--front .brand { left: 40px; top: 118px; }
  .card--back .brand { left: 372px; top: 118px; }

  .motto { position: absolute; left: 330px; top: 44px; line-height: 1; text-transform: uppercase; }
  .motto__light { font-weight: 300; font-size: 22px; color: var(--black); display: block; }
  .motto__bold { font-family: "Archivo Black", sans-serif; font-size: 30px; color: var(--red); display: block; }
  .motto__row { display: flex; align-items: baseline; gap: 10px; }

  .photos { position: absolute; left: 0; top: 208px; width: 650px; height: 130px; display: flex; gap: 5px; }
  .photo { flex: 1; }
  .photo--gate { background: var(--photo-a); flex: 1.2; }
  .photo--panel { background: var(--photo-b); }
  .photo--drive { background: var(--photo-c); flex: .9; }

  .front-web {
    position: absolute; left: 300px; top: 360px; font-size: 17px;
    letter-spacing: 2px; color: var(--black);
  }

  .license { position: absolute; left: 406px; top: 162px; font-size: 15px; color: var(--black); }

  .contacts { position: absolute; left: 58px; top: 268px; font-size: 19px; line-height: 1.2; }
  .contact { display: flex; align-items: flex-start; gap: 12px; margin-bottom: 10px; }
  .contact--tight { margin-bottom: 2px; }
  .contact__icon { width: 18px; height: 18px; flex: none; margin-top: 3px; }
</style>
</head>
<body>
<main class="canvas">

  <section class="card card--front" aria-label="Card front">
    <svg class="card__shapes" viewBox="0 0 700 428" aria-hidden="true">
      <polygon points="530,0 700,0 700,80" fill="var(--black)"/>
      <polygon points="700,70 700,330 610,330" fill="var(--red)"/>
      <polygon points="0,338 250,338 0,428" fill="var(--red)"/>
      <polygon points="0,400 230,428 0,428" fill="var(--red)"/>
    </svg>

    <div class="brand">
      <span class="brand__dot"></span>
      <span class="brand__name">BRANKEL RAILS</span>
    </div>

    <div class="motto">
      <span class="motto__light">Servicing the</span>
      <span class="motto__bold">Peninsula</span>
      <span class="motto__row"><span class="motto__light">For over</span><span class="motto__bold">35 Years</span></span>
    </div>

    <div class="photos">
      <div class="photo photo--gate" role="img" aria-label="Photo of a black metal gate and garden hedge at a home"></div>
      <div class="photo photo--panel" role="img" aria-label="Photo of a dark blue steel panel fence in front of a house"></div>
      <div class="photo photo--drive" role="img" aria-label="Photo of a metal pool fence beside a driveway"></div>
    </div>

    <p class="front-web">www.brankelrails.com.au</p>
  </section>

  <section class="card card--back" aria-label="Card back">
    <svg class="card__shapes" viewBox="0 0 700 428" aria-hidden="true">
      <polygon points="0,0 130,0 50,220 0,220" fill="var(--red)"/>
      <polygon points="0,200 70,200 40,260" fill="var(--black)"/>
      <polygon points="560,0 700,0 700,110" fill="var(--black)"/>
      <polygon points="620,60 700,110 700,428 590,428" fill="var(--red)"/>
    </svg>

    <div class="brand">
      <span class="brand__dot"></span>
      <span class="brand__name">BRANKEL RAILS</span>
    </div>
    <p class="license">LICENSE No. 48215K</p>

    <div class="contacts">
      <div class="contact">
        <svg class="contact__icon" viewBox="0 0 20 20" aria-hidden="true"><path d="M10 1a6 6 0 0 0-6 6c0 5 6 12 6 12s6-7 6-12a6 6 0 0 0-6-6z" fill="var(--red)"/><circle cx="10" cy="7" r="2.3" fill="#fff"/></svg>
        <span>PO Box 148<br>Coralee NSW 2260</span>
      </div>
      <div class="contact contact--tight">
        <svg class="contact__icon" viewBox="0 0 20 20" aria-hidden="true"><path d="M5 2l3 4-2 2c1 3 3 5 6 6l2-2 4 3-2 3C9 18 2 11 2 4z" fill="var(--red)"/></svg>
        <span>(02) 4388 1520</span>
      </div>
      <div class="contact contact--tight">
        <svg class="contact__icon" viewBox="0 0 20 20" aria-hidden="true"><rect x="1" y="4" width="18" height="12" fill="var(--red)"/><path d="M1 4l9 7 9-7" fill="none" stroke="#fff" stroke-width="1.5"/></svg>
        <span>brankelrails@mailbay.com</span>
      </div>
      <div class="contact contact--tight">
        <svg class="contact__icon" viewBox="0 0 20 20" aria-hidden="true"><circle cx="10" cy="10" r="8.5" fill="var(--red)"/><path d="M1.5 10h17M10 1.5v17M4 5h12M4 15h12" stroke="#fff" stroke-width="1.2"/></svg>
        <span>www.brankelrails.com.au</span>
      </div>
    </div>
  </section>

</main>
</body>
</html>
```